Dark Comedy Movie Poster

We need a poster design for our short film BRAM that we just wrapped on.
It's a dark comedy
Bram explores the world of loneliness through the lens of a manic man-child. Bram wants nothing more than the approval of others, giving every last bit of energy to the cause. But his ravenous attempts accomplish the opposite, turning others off. His desperation is authentic, his lonliness cavernous.
Here is a link to the film
https://clipvault.example/548207316
Password: Bram42
I want you, the artist, to pitch me an idea in any way you want. I'm open to absolutely anything right now. Once I have some pitches from you all my production team and I will sort through them and pick the best fit!
-Owen

```html
<!DOCTYPE html>
<html lang="en">
<head>
<meta charset="utf-8">
<title>BRAM — Film Poster</title>
<link href="https://fonts.googleapis.com/css2?family=Varela+Round&family=Nunito+Sans:wght@400;700&display=swap" rel="stylesheet">
<style>
  :root {
    --stage: #dcdcd8;
    --ink: #000000;
    --gold: #c9a13b;
    --cream: #e6dc9e;
    --orange: #e07a2c;
    --rust: #cf5428;
    --copy: #c9671f;
  }
  html, body {
    margin: 0;
    width: 1200px;
    height: 900px;
    overflow: hidden;
    background: var(--stage);
  }
  .poster {
    position: absolute;
    left: 310px;
    top: 20px;
    width: 580px;
    height: 860px;
    background: var(--ink);
    overflow: hidden;
  }
  .poster-art {
    position: absolute;
    inset: 0;
    width: 580px;
    height: 860px;
  }
  .film-title {
    font-family: "Varela Round", sans-serif;
    font-size: 165px;
  }
  .tagline {
    position: absolute;
    left: 0;
    top: 776px;
    width: 470px;
    font-family: "Nunito Sans", sans-serif;
    color: var(--copy);
  }
  .tagline-mark {
    position: absolute;
    left: 0;
    top: 0;
    width: 12px;
    height: 40px;
    background: var(--orange);
  }
  .tagline-lead {
    margin: 0 0 2px 28px;
    font-size: 10px;
    font-weight: 700;
    color: var(--orange);
  }
  .tagline-sub {
    margin: 0 0 4px 28px;
    font-size: 7px;
    font-weight: 700;
  }
  .tagline-body {
    margin: 0 0 0 28px;
    font-size: 5.5px;
    line-height: 1.45;
  }
</style>
</head>
<body>
  <main class="poster">
    <svg class="poster-art" viewBox="0 0 580 860" xmlns="http://www.w3.org/2000/svg">
      <defs>
        <linearGradient id="warm-field" x1="0" y1="0" x2="1" y2="0">
          <stop offset="0" stop-color="var(--gold)"/>
          <stop offset="0.35" stop-color="var(--cream)"/>
          <stop offset="0.65" stop-color="var(--orange)"/>
          <stop offset="1" stop-color="var(--rust)"/>
        </linearGradient>
        <linearGradient id="warm-fade" x1="0" y1="0" x2="0" y2="1">
          <stop offset="0.75" stop-color="#000" stop-opacity="0"/>
          <stop offset="1" stop-color="#000" stop-opacity="0.6"/>
        </linearGradient>
      </defs>

      <g class="key-art" role="img" aria-label="Artwork area: warm gold, cream, orange and rust vertical streaks dripping down behind the black silhouette of a man kneeling with arms spread wide">
        <rect x="96" y="6" width="402" height="594" fill="url(#warm-field)"/>
        <rect x="96" y="6" width="402" height="594" fill="url(#warm-fade)"/>
      </g>

      <text class="film-title" x="88" y="752" textLength="452" lengthAdjust="spacing"><tspan fill="var(--gold)">B</tspan><tspan fill="var(--cream)">R</tspan><tspan fill="var(--orange)">A</tspan><tspan fill="var(--rust)">M</tspan></text>
    </svg>

    <section class="tagline">
      <span class="tagline-mark"></span>
      <p class="tagline-lead">Enter a magical</p>
      <p class="tagline-sub">kingdom where you can sail with pirates, explore exotic jungles, meet fairy tale princesses.</p>
      <p class="tagline-body">Bram spends every waking hour chasing a kind word, a shared laugh, a seat at anyone's table. The harder he tries, the faster the room empties. A short dark comedy about wanting to belong, written and directed by Owen, shot over nine nights in a city that never quite noticed him.</p>
    </section>
  </main>
</body>
</html>
```